Velimko AdAgency Presentation

We need ppt design for an ad agency re-branding, agency is based in Moscow, Russia. Our specifics is brand audit, consulting and strategy in web and offline.
We decided to do re-branding because our current agency does not answer the purpose and we need a kind of "second breath".
The idea of re-branding appeared because of many changes that happened in company: new clients, new projects level, new team.
So we'd like to promote company of changes and design should show this spirit as possible.
You may use info in attached pdf file (sorry for Russian language). Info is not so necessary, it will be replaced later.
Updates

Please use more colors than digital blue and grey!

Industry/Entity Type

Ad Agency

Requirements
Must have
• Logo is attached. Please choose one.

Ppt project should include:
- Front and last page design
- Heading and list design
- Page-separator design
- Diagram design
- Pics appearance

```html
<!DOCTYPE html>
<html lang="en">
<head>
<meta charset="utf-8">
<title>Velimko Presentation Sheet</title>
<link href="https://fonts.googleapis.com/css2?family=Open+Sans:wght@400;600;700;800&display=swap" rel="stylesheet">
<style>
:root{
  --sheet:#1a1a1a;
  --navy:#0b2440;
  --deep:#06182b;
  --blue:#2a8fc9;
  --sky:#5bc1ea;
  --pale:#9fd6f0;
  --violet:#6b2d8c;
  --teal:#1f8a9a;
  --ink:#2b2b2b;
  --muted:#6a6a6a;
  --line:#d9d9d9;
  --white:#ffffff;
}
*{box-sizing:border-box;margin:0;padding:0}
html,body{width:814px;height:1200px;overflow:hidden;background:var(--sheet);font-family:"Open Sans",Arial,sans-serif}
.sheet{width:814px;height:1200px;display:grid;grid-template-columns:repeat(3,256px);grid-template-rows:repeat(6,189px);gap:9px 11px;padding:10px 12px}
.slide{position:relative;overflow:hidden;background:var(--white)}
.slide--dark{background:var(--navy)}
.glow{position:absolute;left:0;right:0;top:0;height:120px;background:linear-gradient(110deg,var(--violet),var(--teal) 50%,#27508f)}
.glow::after{content:"";position:absolute;inset:0;background:linear-gradient(180deg,rgba(11,36,64,0) 20%,var(--navy) 100%)}
.brand{position:absolute;display:flex;flex-direction:column;align-items:center;color:#c9d8e6;font-weight:400}
.brand__mark{width:18px;height:18px;background:#c9d8e6;margin-bottom:3px}
.brand__name{font-size:13px;letter-spacing:.5px}
.cover .brand{left:0;right:0;top:58px}
.cover__info{position:absolute;left:0;right:0;top:112px;text-align:center;color:#8fa6bb;font-size:3.6px;line-height:1.5}
.copy{position:absolute;left:0;right:0;bottom:6px;text-align:center;color:#7d93a8;font-size:3.6px}
.devices{position:absolute;left:92px;top:40px;width:120px;height:70px;border-radius:3px;background:linear-gradient(135deg,#2b2b30,#b5552c 60%,#e0a050)}
.devices-brand{left:40px;top:48px}
.devices-brand .brand__name{font-size:9px}
.devices-brand .brand__mark{width:14px;height:14px}
.arc{position:absolute;left:0;top:0;width:256px;height:189px}
.title-block{position:absolute;left:0;right:0;top:72px;text-align:center}
.title-block .brand{position:static;margin-bottom:6px}
.title-block .brand__mark{width:11px;height:11px;margin-bottom:2px}
.title-block .brand__name{font-size:7px}
.title-main{color:var(--white);font-weight:800;font-size:16px;letter-spacing:.3px}
.title-sub{color:var(--sky);font-size:4.4px;letter-spacing:.4px;margin-top:2px}
.title-by{color:var(--sky);font-size:3.4px;line-height:1.5;margin-top:6px}
.slide--end .copy,.slide--title .copy{color:#8a8a8a;bottom:4px}
.head{position:absolute;left:12px;top:12px;font-size:6.2px;font-weight:700;color:var(--ink);letter-spacing:.1px}
.head::after{content:"";display:block;width:36px;height:1px;background:var(--line);margin-top:4px}
.corner{position:absolute;right:10px;top:8px;display:flex;flex-direction:column;align-items:center}
.corner__mark{width:9px;height:9px;background:var(--blue)}
.corner__name{font-size:3.4px;color:var(--blue);margin-top:1px}
.band{position:absolute;left:0;right:0;bottom:0;height:20px;background:linear-gradient(100deg,var(--violet),var(--teal) 45%,#1b3f72)}
.band__text{position:absolute;left:0;right:0;bottom:7px;text-align:center;color:#dbe6f0;font-size:3.4px}
.band__num{position:absolute;right:14px;bottom:7px;color:#dbe6f0;font-size:3.4px}
.text{position:absolute;font-size:3.5px;line-height:1.45;color:var(--muted);text-align:justify}
.text p+p{margin-top:3px}
.pic{position:absolute;border-radius:1px}
.pic--tower{left:40px;top:48px;width:44px;height:66px;background:linear-gradient(180deg,#3a4f7a,#b58a5a 80%,#2c2a30)}
.pic--group{left:70px;top:44px;width:56px;height:36px;background:linear-gradient(135deg,#e9e4dc,#b98b6c)}
.pic--laptop{background:linear-gradient(135deg,#1e4f86,#5aa0d8)}
.pic--laptop::after{content:"";position:absolute;left:-4px;right:-4px;bottom:-3px;height:3px;background:#c8c8c8;border-radius:0 0 2px 2px}
.pic--stack{left:42px;top:54px;width:62px;height:40px;background:linear-gradient(135deg,#333,#b5552c 60%,#e0a050)}
.caption{position:absolute;font-size:3.5px;line-height:1.45;color:var(--muted);text-align:center}
.caption b,.item b{color:var(--ink);font-weight:700}
.item{position:absolute;left:60px;width:170px;font-size:3.5px;line-height:1.45;color:var(--muted)}
.item b{display:block;font-size:4.4px;color:var(--blue)}
.dot{position:absolute;left:40px;width:11px;height:11px;border-radius:50%;background:var(--blue);color:#fff;font-size:5px;font-weight:700;display:flex;align-items:center;justify-content:center}
.map{position:absolute;left:26px;top:42px;width:180px;height:90px;background:linear-gradient(180deg,#6cc3e6,#45a9d6);border-radius:30px 40px 20px 30px}
.map-label{position:absolute;font-size:3.4px;color:#444;line-height:1.4}
.divider .title-main{font-size:15px}
.graphic{position:absolute}
table.data{position:absolute;border-collapse:collapse;font-size:3.3px;color:var(--muted)}
table.data th{background:#3a9fcf;color:#fff;font-weight:600;text-align:left;padding:1.6px 3px}
table.data td{padding:1.6px 3px;border-bottom:.5px solid #e3e3e3}
table.data tr:nth-child(even) td{background:#eef6fb}
</style>
</head>
<body>
<main class="sheet">

  <!-- 1 cover -->
  <section class="slide slide--dark cover">
    <div class="glow" role="img" aria-label="Soft bokeh lights in violet, teal and blue"></div>
    <div class="brand"><span class="brand__mark"></span><span class="brand__name">Velimko</span></div>
    <div class="cover__info">Your Company Address Here<br>City, 2013<br>+00 000 000 0000<br>+00 000 000 0001</div>
    <div class="copy">© 2013 Velimko All rights reserved.</div>
  </section>

  <!-- 2 devices -->
  <section class="slide slide--dark">
    <div class="glow" role="img" aria-label="Soft bokeh lights in violet, teal and blue"></div>
    <div class="brand devices-brand"><span class="brand__mark"></span><span class="brand__name">Velimko</span></div>
    <div class="devices" role="img" aria-label="Laptop, tablet, monitor and phone showing sunset industry photos"></div>
    <div class="copy">© 2013 Velimko All rights reserved.</div>
  </section>

  <!-- 3 title -->
  <section class="slide slide--dark slide--title">
    <div class="glow" role="img" aria-label="Soft bokeh lights in violet, teal and blue"></div>
    <svg class="arc" viewBox="0 0 256 189" aria-hidden="true">
      <defs><linearGradient id="arcFill" x1="0" y1="0" x2="0" y2="1"><stop offset="0" stop-color="#1a4670"/><stop offset="1" stop-color="#0b2440"/></linearGradient></defs>
      <path d="M0 120 Q128 40 256 120 L256 176 L0 176 Z" fill="url(#arcFill)"/>
      <path d="M0 172 Q128 158 256 172 L256 189 L0 189 Z" fill="#ffffff"/>
    </svg>
    <div class="title-block">
      <div class="brand"><span class="brand__mark"></span><span class="brand__name">Velimko</span></div>
      <div class="title-main">YOUR TITTLE HERE</div>
      <div class="title-sub">YOUR PRESENTATION SUB TITLE HERE</div>
      <div class="title-by">Written By:<br>Mr. Lorem Daniels<br>Manager Position<br>+00 000 000 000</div>
    </div>
    <div class="copy">© 2013 Velimko All rights reserved.</div>
  </section>

  <!-- 4 picture + text -->
  <section class="slide">
    <h2 class="head">VELIMKO PRESENTATION POWERFUL MISSION 1</h2>
    <div class="corner"><span class="corner__mark"></span><span class="corner__name">Velimko</span></div>
    <div class="pic pic--tower" role="img" aria-label="Office tower lit at dusk"></div>
    <div class="text" style="left:98px;top:50px;width:120px">
      <p>Velimko builds brands that move. We audit, consult and plan strategy for web and offline, giving every client a clear voice, a fresh start and steady growth in a fast changing market.</p>
      <p>Each project begins with research and honest talk. Our team turns insight into ideas, ideas into campaigns, and campaigns into results that clients can measure and share with pride.</p>
    </div>
    <div class="band" role="img" aria-label="Bokeh light band"></div>
    <div class="band__text">© 2013 Velimko All rights reserved.</div><div class="band__num">1</div>
  </section>

  <!-- 5 picture + two columns -->
  <section class="slide">
    <h2 class="head">VELIMKO PRESENTATION POWERFUL MISSION 1</h2>
    <div class="corner"><span class="corner__mark"></span><span class="corner__name">Velimko</span></div>
    <div class="pic pic--group" role="img" aria-label="Team of three colleagues at a desk"></div>
    <div class="text" style="left:70px;top:86px;width:62px">
      <p>Velimko builds brands that move. We audit and plan for web and offline, giving clients a fresh start.</p>
      <p>Our team turns insight into ideas and ideas into campaigns with results clients can measure.</p>
    </div>
    <div class="text" style="left:140px;top:44px;width:76px">
      <p>Velimko builds brands that move. We audit, consult and plan strategy for web and offline, giving every client a clear voice and a fresh start.</p>
      <p>Each project begins with research and honest talk, then grows into a plan the whole team believes in.</p>
    </div>
    <div class="band" role="img" aria-label="Bokeh light band"></div>
    <div class="band__text">© 2013 Velimko All rights reserved.</div><div class="band__num">2</div>
  </section>

  <!-- 6 numbered list -->
  <section class="slide">
    <h2 class="head">VELIMKO PRESENTATION POWERFUL MISSION 1</h2>
    <div class="corner"><span class="corner__mark"></span><span class="corner__name">Velimko</span></div>
    <span class="dot" style="top:48px">1</span>
    <div class="item" style="top:46px"><b>We know firsthand 1</b>Since 2013 we have guided brands through every stage of change, from the first audit to the final launch.</div>
    <span class="dot" style="top:80px">2</span>
    <div class="item" style="top:78px"><b>We know firsthand 2</b>Since 2013 we have guided brands through every stage of change, from the first audit to the final launch, with care and a clear plan for growth.</div>
    <span class="dot" style="top:116px">3</span>
    <div class="item" style="top:114px"><b>We know firsthand 3</b>Since 2013 we have guided brands through every stage of change, from the first audit to the final launch.</div>
    <div class="band" role="img" aria-label="Bokeh light band"></div>
    <div class="band__text">© 2013 Velimko All rights reserved.</div><div class="band__num">3</div>
  </section>

  <!-- 7 three laptops -->
  <section class="slide">
    <h2 class="head">VELIMKO PRESENTATION POWERFUL MISSION 1</h2>
    <div class="corner"><span class="corner__mark"></span><span class="corner__name">Velimko</span></div>
    <div class="pic pic--laptop" style="left:54px;top:58px;width:38px;height:24px" role="img" aria-label="Laptop showing a blue screen"></div>
    <div class="pic pic--laptop" style="left:110px;top:58px;width:38px;height:24px" role="img" aria-label="Laptop showing a blue screen"></div>
    <div class="pic pic--laptop" style="left:166px;top:58px;width:38px;height:24px" role="img" aria-label="Laptop showing a blue screen"></div>
    <div class="caption" style="left:44px;top:92px;width:58px"><b>Fall Sale in Moscow</b><br>new ideas for every brand, fresh looks and bold plans for the season ahead.</div>
    <div class="caption" style="left:100px;top:92px;width:58px"><b>Fall Sale in Moscow</b><br>new ideas for every brand, fresh looks and bold plans.</div>
    <div class="caption" style="left:156px;top:92px;width:58px"><b>Fall Sale in Moscow</b><br>new ideas for every brand, fresh looks and bold plans for the season.</div>
    <div class="band" role="img" aria-label="Bokeh light band"></div>
    <div class="band__text">© 2013 Velimko All rights reserved.</div><div class="band__num">4</div>
  </section>

  <!-- 8 devices + text -->
  <section class="slide">
    <h2 class="head">VELIMKO PRESENTATION POWERFUL MISSION 1</h2>
    <div class="corner"><span class="corner__mark"></span><span class="corner__name">Velimko</span></div>
    <div class="pic pic--stack" role="img" aria-label="Group of screens and devices showing campaign photos"></div>
    <div class="text" style="left:126px;top:46px;width:92px">
      <p>Velimko builds brands that move. We audit, consult and plan strategy for web and offline, giving every client a clear voice and a fresh start in a changing market.</p>
      <p>Each project begins with research and honest talk. Our team turns insight into ideas and ideas into campaigns that clients can measure.</p>
    </div>
    <div class="band" role="img" aria-label="Bokeh light band"></div>
    <div class="band__text">© 2013 Velimko All rights reserved.</div><div class="band__num">5</div>
  </section>

  <!-- 9 stacked laptops -->
  <section class="slide">
    <h2 class="head">VELIMKO PRESENTATION POWERFUL MISSION 1</h2>
    <div class="corner"><span class="corner__mark"></span><span class="corner__name">Velimko</span></div>
    <div class="pic pic--laptop" style="left:104px;top:42px;width:30px;height:19px" role="img" aria-label="Laptop showing a blue screen"></div>
    <div class="pic pic--laptop" style="left:74px;top:80px;width:30px;height:19px" role="img" aria-label="Laptop showing a blue screen"></div>
    <div class="pic pic--laptop" style="left:104px;top:116px;width:30px;height:19px" role="img" aria-label="Laptop showing a blue screen"></div>
    <div class="text" style="left:142px;top:42px;width:80px;text-align:left"><b>Fall Sale in Moscow</b><br>new ideas for every brand and bold plans for the season ahead.</div>
    <div class="text" style="left:112px;top:80px;width:80px;text-align:left"><b>Fall Sale in Moscow</b><br>new ideas for every brand and bold plans for the season.</div>
    <div class="text" style="left:142px;top:116px;width:80px;text-align:left"><b>Fall Sale in Moscow</b><br>new ideas for every brand and bold plans for the season ahead.</div>
    <div class="band" role="img" aria-label="Bokeh light band"></div>
    <div class="band__text">© 2013 Velimko All rights reserved.</div><div class="band__num">6</div>
  </section>

  <!-- 10 world map -->
  <section class="slide">
    <h2 class="head">VELIMKO PRESENTATION POWERFUL MISSION 1</h2>
    <div class="corner"><span class="corner__mark"></span><span class="corner__name">Velimko</span></div>
    <div class="map" role="img" aria-label="Light blue world map with regional percentages"></div>
    <div class="map-label" style="left:24px;top:118px">Europe 24%<br>Asia 31%<br>Americas 45%</div>
    <div class="map-label" style="left:180px;top:66px">Offices 12<br>Clients 80</div>
    <div class="band" role="img" aria-label="Bokeh light band"></div>
    <div class="band__text">© 2013 Velimko All rights reserved.</div><div class="band__num">7</div>
  </section>

  <!-- 11 divider -->
  <section class="slide slide--dark slide--title divider">
    <div class="glow" role="img" aria-label="Soft bokeh lights in violet, teal and blue"></div>
    <svg class="arc" viewBox="0 0 256 189" aria-hidden="true">
      <path d="M0 120 Q128 40 256 120 L256 176 L0 176 Z" fill="url(#arcFill)"/>
      <path d="M0 172 Q128 158 256 172 L256 189 L0 189 Z" fill="#ffffff"/>
    </svg>
    <div class="title-block" style="top:62px">
      <div class="brand"><span class="brand__mark"></span><span class="brand__name">Velimko</span></div>
      <div class="title-main">DIVIDER PAGESHERE</div>
      <div class="title-sub">YOUR PRESENTATION SUB TITLE HERE</div>
    </div>
    <div class="copy">© 2013 Velimko All rights reserved.</div>
  </section>

  <!-- 12 process circles -->
  <section class="slide">
    <div class="corner"><span class="corner__mark"></span><span class="corner__name">Velimko</span></div>
    <svg class="graphic" style="left:48px;top:20px" width="160" height="50" viewBox="0 0 160 50" aria-label="Five process steps">
      <g font-family="Open Sans, sans-serif" font-size="4" font-weight="700" fill="#fff" text-anchor="middle">
        <circle cx="20" cy="25" r="19" fill="#1f4f86"/><text x="20" y="26.5">BRIEF</text>
        <circle cx="50" cy="25" r="19" fill="#2a6aa8" opacity=".95"/><text x="50" y="26.5">ANALISE</text>
        <circle cx="80" cy="25" r="19" fill="#2f86c4" opacity=".95"/><text x="80" y="26.5">DESIGN</text>
        <circle cx="110" cy="25" r="19" fill="#4aa5d8" opacity=".95"/><text x="110" y="26.5">DEVELOP</text>
        <circle cx="140" cy="25" r="19" fill="#79c2e8" opacity=".95"/><text x="140" y="26.5">TESTING</text>
      </g>
    </svg>
    <div class="text" style="left:40px;top:82px;width:176px">
      <p>Velimko builds brands that move. We audit, consult and plan strategy for web and offline, giving every client a clear voice, a fresh start and steady growth in a fast changing market.</p>
      <p>Each project begins with research and honest talk. Our team turns insight into ideas and ideas into campaigns clients can measure.</p>
    </div>
    <div class="band" role="img" aria-label="Bokeh light band"></div>
    <div class="band__text">© 2013 Velimko All rights reserved.</div><div class="band__num">8</div>
  </section>

  <!-- 13 layered diagram -->
  <section class="slide">
    <h2 class="head">VELIMKO PRESENTATION POWERFUL MISSION 1</h2>
    <div class="corner"><span class="corner__mark"></span><span class="corner__name">Velimko</span></div>
    <svg class="graphic" style="left:28px;top:38px" width="90" height="100" viewBox="0 0 90 100" aria-label="Layered process diagram">
      <g font-family="Open Sans, sans-serif" font-size="3.6" font-weight="700" text-anchor="middle">
        <ellipse cx="45" cy="50" rx="42" ry="48" fill="#e6e6e6"/>
        <ellipse cx="45" cy="58" rx="36" ry="40" fill="#cfd8df"/>
        <ellipse cx="45" cy="66" rx="30" ry="32" fill="#7fc3e6"/>
        <ellipse cx="45" cy="74" rx="24" ry="24" fill="#3a9fd6"/>
        <ellipse cx="45" cy="82" rx="18" ry="16" fill="#1f72b4"/>
        <text x="45" y="10" fill="#555">BRIEF</text>
        <text x="45" y="24" fill="#555">ANALISE</text>
        <text x="45" y="40" fill="#fff">DESIGN</text>
        <text x="45" y="57" fill="#fff">DEVELOP</text>
        <text x="45" y="84" fill="#fff">TESTING</text>
      </g>
    </svg>
    <svg class="graphic" style="left:124px;top:44px" width="110" height="100" viewBox="0 0 110 100" aria-label="Bullet list">
      <g font-family="Open Sans, sans-serif" font-size="3.6" fill="#666">
        <circle cx="2" cy="4" r="1.2" fill="#2a8fc9"/><text x="6" y="5.2">Since 2013, we have guided brands</text>
        <circle cx="2" cy="12" r="1.2" fill="#2a8fc9"/><text x="6" y="13.2">Audit and research come first</text>
        <circle cx="2" cy="20" r="1.2" fill="#2a8fc9"/><text x="6" y="21.2">Strategy for web and offline</text>
        <circle cx="2" cy="28" r="1.2" fill="#2a8fc9"/><text x="6" y="29.2">Since 2013, we have guided brands</text>
        <circle cx="2" cy="36" r="1.2" fill="#2a8fc9"/><text x="6" y="37.2">Clear plans for every client</text>
        <circle cx="2" cy="44" r="1.2" fill="#2a8fc9"/><text x="6" y="45.2">Bold ideas, measured results</text>
        <circle cx="2" cy="52" r="1.2" fill="#2a8fc9"/><text x="6" y="53.2">A new team with fresh eyes</text>
        <circle cx="2" cy="60" r="1.2" fill="#2a8fc9"/><text x="6" y="61.2">Multiple projects every season</text>
        <circle cx="2" cy="68" r="1.2" fill="#2a8fc9"/><text x="6" y="69.2">Since 2013, we have guided brands</text>
        <circle cx="2" cy="76" r="1.2" fill="#2a8fc9"/><text x="6" y="77.2">Audit and research come first</text>
        <circle cx="2" cy="84" r="1.2" fill="#2a8fc9"/><text x="6" y="85.2">Strategy for web and offline</text>
      </g>
    </svg>
    <div class="band" role="img" aria-label="Bokeh light band"></div>
    <div class="band__text">© 2013 Velimko All rights reserved.</div><div class="band__num">9</div>
  </section>

  <!-- 14 pie chart -->
  <section class="slide">
    <h2 class="head">VELIMKO PRESENTATION POWERFUL MISSION 1</h2>
    <div class="corner"><span class="corner__mark"></span><span class="corner__name">Velimko</span></div>
    <div class="text" style="left:38px;top:44px;width:82px">
      <p>Velimko builds brands that move. We audit, consult and plan strategy for web and offline, giving every client a clear voice and a fresh start.</p>
      <p>Each project begins with research and honest talk. Our team turns insight into ideas and ideas into campaigns that clients can measure and share.</p>
    </div>
    <svg class="graphic" style="left:132px;top:50px" width="96" height="80" viewBox="0 0 96 80" aria-label="Pie chart in four parts">
      <ellipse cx="48" cy="38" rx="36" ry="26" fill="#1b4f86"/>
      <ellipse cx="48" cy="34" rx="36" ry="26" fill="#2f8fd0"/>
      <path d="M48 34 L48 8 A36 26 0 0 0 14 26 Z" fill="#8c8c8c"/>
      <path d="M48 34 L14 26 A36 26 0 0 0 20 50 Z" fill="#c4c4c4"/>
      <path d="M48 34 L48 8 A36 26 0 0 1 76 18 Z" fill="#5ab2e2"/>
      <g font-family="Open Sans, sans-serif" font-size="3" fill="#888">
        <rect x="6" y="72" width="3" height="3" fill="#2f8fd0"/><text x="11" y="74.6">Web</text>
        <rect x="26" y="72" width="3" height="3" fill="#8c8c8c"/><text x="31" y="74.6">Print</text>
        <rect x="48" y="72" width="3" height="3" fill="#c4c4c4"/><text x="53" y="74.6">Outdoor</text>
        <rect x="72" y="72" width="3" height="3" fill="#5ab2e2"/><text x="77" y="74.6">TV</text>
      </g>
    </svg>
    <div class="band" role="img" aria-label="Bokeh light band"></div>
    <div class="band__text">© 2013 Velimko All rights reserved.</div><div class="band__num">10</div>
  </section>

  <!-- 15 bar chart -->
  <section class="slide">
    <h2 class="head">VELIMKO PRESENTATION POWERFUL MISSION 1</h2>
    <div class="corner"><span class="corner__mark"></span><span class="corner__name">Velimko</span></div>
    <div class="text" style="left:38px;top:44px;width:80px">
      <p>Velimko builds brands that move. We audit, consult and plan strategy for web and offline, giving every client a clear voice and a fresh start.</p>
      <p>Each project begins with research and honest talk. Our team turns insight into ideas and ideas into campaigns that clients can measure.</p>
    </div>
    <svg class="graphic" style="left:134px;top:42px" width="96" height="90" viewBox="0 0 96 90" aria-label="Bar chart rising in five steps">
      <rect x="6" y="58" width="12" height="14" fill="#8a8a8a"/><rect x="18" y="60" width="4" height="12" fill="#6a6a6a"/>
      <rect x="24" y="52" width="12" height="20" fill="#a3a3a3"/><rect x="36" y="54" width="4" height="18" fill="#7d7d7d"/>
      <rect x="42" y="38" width="12" height="34" fill="#7fc3e6"/><rect x="54" y="40" width="4" height="32" fill="#4d9fcf"/>
      <rect x="60" y="24" width="12" height="48" fill="#3a9fd6"/><rect x="72" y="26" width="4" height="46" fill="#1f72b4"/>
      <rect x="78" y="8" width="12" height="64" fill="#2f86c4"/><rect x="90" y="10" width="4" height="62" fill="#1b4f86"/>
      <g font-family="Open Sans, sans-serif" font-size="2.8" fill="#888">
        <text x="6" y="80">2009</text><text x="24" y="80">2010</text><text x="42" y="80">2011</text><text x="60" y="80">2012</text><text x="78" y="80">2013</text>
      </g>
    </svg>
    <div class="band" role="img" aria-label="Bokeh light band"></div>
    <div class="band__text">© 2013 Velimko All rights reserved.</div><div class="band__num">11</div>
  </section>

  <!-- 16 text + table -->
  <section class="slide">
    <div class="corner"><span class="corner__mark"></span><span class="corner__name">Velimko</span></div>
    <div class="text" style="left:40px;top:44px;width:72px">
      <p>Velimko builds brands that move. We audit, consult and plan strategy for web and offline, giving every client a clear voice.</p>
      <p>Each project begins with research and honest talk. Our team turns insight into ideas and ideas into campaigns clients can measure.</p>
    </div>
    <table class="data" style="left:124px;top:40px;width:96px">
      <tr><th>No</th><th>Name</th><th>Date</th><th>Case</th></tr>
      <tr><td>01</td><td>Anna Petrova</td><td>27-06-13</td><td>Open</td></tr>
      <tr><td>02</td><td>Ivan Sokolov</td><td>27-06-13</td><td>Open</td></tr>
      <tr><td>03</td><td>Anna Petrova</td><td>27-06-13</td><td>Close</td></tr>
      <tr><td>04</td><td>Ivan Sokolov</td><td>27-06-13</td><td>Open</td></tr>
      <tr><td>05</td><td>Anna Petrova</td><td>27-06-13</td><td>Close</td></tr>
      <tr><td>06</td><td>Ivan Sokolov</td><td>27-06-13</td><td>Open</td></tr>
      <tr><td>07</td><td>Anna Petrova</td><td>27-06-13</td><td>Close</td></tr>
      <tr><td>08</td><td>Ivan Sokolov</td><td>27-06-13</td><td>Open</td></tr>
    </table>
    <div class="band" role="img" aria-label="Bokeh light band"></div>
    <div class="band__text">© 2013 Velimko All rights reserved.</div><div class="band__num">12</div>
  </section>

  <!-- 17 table + text -->
  <section class="slide">
    <h2 class="head">VELIMKO PRESENTATION POWERFUL MISSION 1</h2>
    <div class="corner"><span class="corner__mark"></span><span class="corner__name">Velimko</span></div>
    <table class="data" style="left:40px;top:40px;width:176px">
      <tr><th>No</th><th>Name</th><th>ID Code</th><th>Address</th><th>Date</th><th>Case</th></tr>
      <tr><td>01</td><td>Anna Petrova</td><td>413056</td><td>Tverskaya St 14</td><td>27-06-13</td><td>Open</td></tr>
      <tr><td>02</td><td>Ivan Sokolov</td><td>413056</td><td>Arbat St 20</td><td>27-06-13</td><td>Open</td></tr>
      <tr><td>03</td><td>Anna Petrova</td><td>413056</td><td>Lenina St 6</td><td>27-06-13</td><td>Close</td></tr>
      <tr><td>04</td><td>Ivan Sokolov</td><td>413056</td><td>Mira Ave 31</td><td>27-06-13</td><td>Open</td></tr>
      <tr><td>05</td><td>Anna Petrova</td><td>413056</td><td>Sadovaya St 9</td><td>27-06-13</td><td>Close</td></tr>
    </table>
    <div class="text" style="left:40px;top:110px;width:176px">
      <p>Velimko builds brands that move. We audit, consult and plan strategy for web and offline, giving every client a clear voice and a fresh start in a changing market.</p>
      <p>Each project begins with research and honest talk, then grows into a plan the team believes in.</p>
    </div>
    <div class="band" role="img" aria-label="Bokeh light band"></div>
    <div class="band__text">© 2013 Velimko All rights reserved.</div><div class="band__num">13</div>
  </section>

  <!-- 18 closing -->
  <section class="slide slide--dark slide--end">
    <div class="glow" role="img" aria-label="Soft bokeh lights in violet, teal and blue"></div>
    <svg class="arc" viewBox="0 0 256 189" aria-hidden="true">
      <path d="M0 120 Q128 40 256 120 L256 176 L0 176 Z" fill="url(#arcFill)"/>
      <path d="M0 172 Q128 158 256 172 L256 189 L0 189 Z" fill="#ffffff"/>
    </svg>
    <div class="title-block">
      <div class="brand"><span class="brand__mark"></span><span class="brand__name">Velimko</span></div>
      <div class="title-main">THANK YOU</div>
      <div class="title-sub">YOUR PRESENTATION SUB TITLE HERE</div>
      <div class="title-by">Written By:<br>Mr. Lorem Daniels<br>Manager Position<br>+00 000 000 000</div>
    </div>
    <div class="copy">© 2013 Velimko All rights reserved.</div>
  </section>

</main>
</body>
</html>
```